I am a home builder and developer

I would like some sort of architectural design like a pencil type of drawing of a house but want it to be professional looking and two sided.

Simply I am a custom home builder and land developer. I would like a new design other than what I have now that's what I thought y'all did. I like mostly black maybe with an pencil type of drawing of a house. Like an architectural look.

Industry/Entity Type

Home Builder

```html
<!DOCTYPE html>
<html lang="en">
<head>
<meta charset="UTF-8">
<title>R &amp; K Costruzio Inc — Business Card</title>
<link rel="stylesheet" href="https://fonts.googleapis.com/css2?family=Comfortaa:wght@500&family=Roboto+Mono:wght@500;700&display=swap">
<style>
  :root {
    --card-black: #000000;
    --page-white: #ffffff;
    --ink-white: #ffffff;
    --mark-grey: #7b7b7b;
  }
  * { margin: 0; padding: 0; box-sizing: border-box; }
  html, body {
    width: 1091px;
    height: 1200px;
    overflow: hidden;
    background: var(--page-white);
  }
  .sheet {
    position: relative;
    width: 1091px;
    height: 1200px;
  }
  .card {
    position: absolute;
    left: 0;
    width: 1091px;
    background: var(--card-black);
    border-radius: 100px;
    overflow: hidden;
  }
  .card--front { top: 0; height: 577px; }
  .card--back { top: 630px; height: 570px; }

  .brand-name {
    position: absolute;
    left: 0;
    right: 0;
    top: 38px;
    text-align: center;
    font-family: "Comfortaa", sans-serif;
    font-weight: 500;
    color: var(--ink-white);
    font-size: 76px;
    line-height: 124px;
    letter-spacing: 1px;
  }
  .brand-mark {
    position: absolute;
    left: 435px;
    top: 326px;
    width: 222px;
    height: 222px;
    background: var(--mark-grey);
    border-radius: 8px;
  }

  .person-pill {
    position: absolute;
    left: 329px;
    top: 97px;
    width: 438px;
    height: 64px;
    border-radius: 16px;
    background: var(--mark-grey);
    color: var(--ink-white);
    font-family: "Roboto Mono", monospace;
    font-weight: 500;
    font-size: 42px;
    line-height: 64px;
    text-align: center;
  }
  .contact {
    position: absolute;
    left: 0;
    right: 0;
    top: 225px;
    text-align: center;
    font-family: "Roboto Mono", monospace;
    font-weight: 700;
    color: var(--ink-white);
    font-size: 43px;
    line-height: 67px;
  }
</style>
</head>
<body>
  <main class="sheet">
    <section class="card card--front" aria-label="Card front">
      <h1 class="brand-name">R &amp; K<br>Costruzio Inc</h1>
      <div class="brand-mark" role="img" aria-label="Company building mark"></div>
    </section>

    <section class="card card--back" aria-label="Card back">
      <p class="person-pill">Daniel Verner</p>
      <p class="contact">
        <span class="contact__phone">555-204-3187</span><br>
        <span class="contact__email">Rkbuildinc@mailnest.com</span>
      </p>
    </section>
  </main>
</body>
</html>
```